Business card design needed

Chasing a very simplistic modern design with a logo incorporating "RTK".
I'm starting a plumbing business.
I do water, sanitary and drainage plumbing that will cover residential, commercial, rental, rural, excavation, new housing and all maintanence requirements.

Industry/Entity Type

Business

Contact Information for Business Card

RTK PLUMBING SERVICES
DAVID TRELOWEN - LICENSED PLUMBER
PHONE: 0481956274
E-MAIL: trelodw7@kestrelnet.com
NORTHERN SUBURBS

Requirements
Must have
• lower case email address

```html
<!DOCTYPE html>
<html lang="en">
<head>
<meta charset="utf-8">
<title>RTK Plumbing Services – Business Card</title>
<link rel="stylesheet" href="https://fonts.googleapis.com/css2?family=Michroma&family=Arimo:wght@700&display=swap">
<style>
  :root {
    --paper: #ffffff;
    --ink: #000000;
    --pipe: #b5b5b7;
    --muted: #a9a9ab;
    --contact: #e8e8e8;
    --edge: #d6d6d6;
  }
  * { margin: 0; padding: 0; box-sizing: border-box; }
  html, body {
    width: 1200px;
    height: 341px;
    overflow: hidden;
    background: var(--paper);
  }
  .sheet {
    position: relative;
    width: 1200px;
    height: 341px;
  }
  .card {
    position: absolute;
    top: 0;
    width: 590px;
    height: 341px;
    overflow: hidden;
    border: 1px solid var(--edge);
  }

  /* Front */
  .card--front { left: 0; background: var(--paper); }
  .brand-mark {
    position: absolute;
    top: 14px;
    left: 0;
    width: 100%;
    text-align: center;
    font-family: "Michroma", sans-serif;
    font-size: 150px;
    line-height: 190px;
    letter-spacing: 6px;
    color: var(--ink);
  }
  .brand-line {
    position: absolute;
    top: 206px;
    left: 0;
    width: 100%;
    text-align: center;
    font-family: "Michroma", sans-serif;
    font-size: 30px;
    line-height: 40px;
    color: var(--ink);
    font-variant: small-caps;
  }
  .services-band {
    position: absolute;
    left: 0;
    bottom: 0;
    width: 100%;
    height: 93px;
    background: var(--ink);
    padding-top: 13px;
    text-align: center;
    color: var(--paper);
    font-family: "Michroma", sans-serif;
    font-size: 10px;
    line-height: 17.5px;
    text-transform: uppercase;
    letter-spacing: 0.3px;
  }

  /* Back */
  .card--back { left: 610px; background: var(--ink); }
  .header-art {
    position: absolute;
    top: 0;
    left: 0;
    width: 100%;
    height: 138px;
    background: linear-gradient(180deg, var(--paper) 0%, var(--paper) 60%, var(--pipe) 100%);
  }
  .holder-name {
    position: absolute;
    top: 35px;
    left: 0;
    width: 100%;
    text-align: center;
    font-family: "Michroma", sans-serif;
    font-weight: 400;
    font-size: 27px;
    line-height: 34px;
    font-variant: small-caps;
    color: var(--ink);
  }
  .holder-title {
    position: absolute;
    top: 69px;
    left: 0;
    width: 100%;
    text-align: center;
    font-family: "Michroma", sans-serif;
    font-size: 18px;
    line-height: 22px;
    font-variant: small-caps;
    color: var(--muted);
  }
  .contact {
    position: absolute;
    top: 192px;
    left: 0;
    width: 100%;
    text-align: center;
    list-style: none;
    font-family: "Arimo", Arial, sans-serif;
    font-weight: 700;
    font-size: 18px;
    line-height: 26px;
    color: var(--contact);
  }
  .contact .area { margin-top: 12px; }
</style>
</head>
<body>
<main class="sheet">

  <section class="card card--front" aria-label="Card front">
    <div class="brand-mark">RTK</div>
    <div class="brand-line">Plumbing Services</div>
    <p class="services-band">
      Water, sanitary and drainage plumbing that will cover<br>
      residential, commercial, rental, rural, excavation, new<br>
      housing and all maintanence requirements.
    </p>
  </section>

  <section class="card card--back" aria-label="Card back">
    <div class="header-art" role="img" aria-label="Grey pipe frame illustration framing the name panel"></div>
    <h1 class="holder-name">David Trelowen</h1>
    <p class="holder-title">Licensed Plumber</p>
    <ul class="contact">
      <li>PHONE: 0481956274</li>
      <li>E-MAIL: trelodw7@kestrelnet.com</li>
      <li class="area">NORTHERN SUBURBS</li>
    </ul>
  </section>

</main>
</body>
</html>
```